Creating the Look and Feel of an Elite Boutique Consulting Practice: Kestrel Advisory

Complete a professional website on Weebly. As part of the site, we are open to a new logo -- we have just launched. We put up a starter website that shows you the content and theme we are going for. But clearly we aren't professional web designers and we need your help. Check out our start at kestreladvisory.com

Target Market(s)

Fortune 500 Clients

Industry/Entity Type

Management Consulting

Logo Text

KESTREL Advisory

Number of Pages Required

4 page

Requirements
Must have
• I've already set us up on Weebly. I'd like to give the selected designer the log-in credentials and have the designer create it on Weebly, so we can maintain it through that service.

```html
<!DOCTYPE html>
<html lang="en">
<head>
<meta charset="utf-8">
<title>Kestrel Advisory</title>
<link href="https://fonts.googleapis.com/css2?family=Lato:ital,wght@0,400;0,700;0,900;1,400;1,700&display=swap" rel="stylesheet">
<style>
:root{
  --ink:#000;
  --bar:#030303;
  --accent:#6ba2c6;
  --muted:#b3b3b3;
  --btn-grey:#c2c2c2;
  --btn-grey-text:#555;
  --rule:#555;
  --footer-text:#bdbdbd;
  --white:#fff;
}
*{margin:0;padding:0;box-sizing:border-box}
html,body{width:802px;height:1200px;overflow:hidden;background:var(--white)}
body{font-family:'Lato',sans-serif;color:var(--ink);position:relative}
.site-header{position:absolute;top:0;left:0;width:802px;height:47px;background:var(--bar)}
.brand{position:absolute;left:85px;top:12px;font-size:17px;font-weight:400;color:var(--white);letter-spacing:.5px;display:flex;align-items:center;gap:7px}
.brand-dot{width:9px;height:9px;border-radius:50%;background:var(--accent)}
.main-nav{position:absolute;right:84px;top:18px;display:flex;gap:17px}
.main-nav a,.footer-nav a{color:#d6d6d6;text-decoration:none;font-size:8.5px;font-weight:700;letter-spacing:.2px}
.hero{position:absolute;top:47px;left:0;width:802px;height:341px;
  background:radial-gradient(ellipse at 60% 30%,#7d7670 0%,#5a544f 45%,#3a3633 100%)}
.hero-kicker{position:absolute;top:112px;width:100%;text-align:center;color:var(--white);font-style:italic;font-size:19.5px}
.hero-title{position:absolute;top:141px;width:100%;text-align:center;color:var(--white);font-weight:900;font-size:28.5px;letter-spacing:-.3px}
.hero-title span{color:var(--accent)}
.btn{display:flex;align-items:center;justify-content:center;font-size:8.5px;font-weight:900;text-decoration:none;letter-spacing:-.1px}
.btn-blue{background:var(--accent);color:var(--white)}
.btn-grey{background:var(--btn-grey);color:var(--btn-grey-text)}
.hero .btn{position:absolute;left:350px;top:191px;width:104px;height:29px}
.section-head{position:absolute;left:85px;width:633px;height:20px;border-bottom:1px solid var(--rule)}
.section-head h2{position:absolute;left:0;right:0;top:-5px;text-align:center;font-size:20.5px;font-weight:900;color:var(--muted);letter-spacing:-.3px}
.section-head::after{content:"";position:absolute;left:50%;margin-left:-29px;bottom:-2px;width:58px;height:3px;background:var(--accent)}
.lead{position:absolute;top:490px;width:100%;text-align:center;font-size:14.5px;font-weight:900}
.service{position:absolute;top:518px;width:150px;text-align:center;font-size:9.4px;line-height:13px}
.service-icon{width:88px;height:88px;border:1px solid var(--accent);border-radius:50%;margin:0 auto 8px;display:flex;align-items:center;justify-content:center}
.service em{display:block;font-weight:700}
.approach-btn{position:absolute;left:327px;top:737px;width:147px;height:29px}
.who-title{position:absolute;top:869px;width:100%;text-align:center;font-size:14.5px;font-weight:400;color:var(--accent)}
.who-title b{font-weight:700}
.who-title strong{color:var(--ink);font-weight:900}
.who-copy{position:absolute;left:85px;top:896px;width:465px;font-size:9.3px;line-height:13px}
.who-copy h3{font-size:9.4px;font-style:italic;font-weight:900}
.who-copy p{margin-bottom:13px}
.team-btn{position:absolute;left:576px;top:935px;width:142px;height:29px}
.contact-btn{position:absolute;left:576px;top:970px;width:142px;height:29px}
.site-footer{position:absolute;top:1094px;left:0;width:802px;height:106px;background:var(--bar);text-align:center}
.footer-nav{position:absolute;top:22px;width:100%;display:flex;justify-content:center;gap:17px}
.social{position:absolute;top:40px;width:100%;display:flex;justify-content:center;gap:4px}
.social span{width:14px;height:14px;border-radius:50%;background:#cfcfcf}
.contact-line{position:absolute;top:59px;width:100%;font-size:8.3px;font-weight:700;color:var(--footer-text)}
.copyright{position:absolute;top:76px;width:100%;font-size:6.5px;color:#999}
</style>
</head>
<body>
<header class="site-header">
  <div class="brand"><span>KESTREL ADVISORY</span><i class="brand-dot"></i></div>
  <nav class="main-nav"><a href="#">ABOUT KESTREL</a><a href="#">APPROACH</a><a href="#">TEAM</a><a href="#">CONTACT</a></nav>
</header>

<section class="hero" role="img" aria-label="Photograph of a compass and rolled antique maps in muted sepia tones">
  <p class="hero-kicker">Do you need to transform your organization?</p>
  <h1 class="hero-title">LET'S <span>CHART</span> YOUR PATH TO SUCCESS!</h1>
  <a class="btn btn-blue" href="#">CONTACT US »</a>
</section>

<div class="section-head" style="top:449px"><h2>WHAT WE DO</h2></div>
<p class="lead">We help your organization achieve a successful, resilient transformation!</p>

<div class="service" style="left:80px">
  <div class="service-icon"><svg width="50" height="42" viewBox="0 0 50 42"><rect x="14" y="2" width="34" height="22" rx="2" fill="#6ba2c6"/><path d="M40 24l6 6v-6z" fill="#6ba2c6"/><rect x="2" y="10" width="34" height="22" rx="2" fill="#6ba2c6" stroke="#fff" stroke-width="2"/><path d="M8 32l-2 8 9-8z" fill="#6ba2c6"/></svg></div>
  Partnering with you to clarify and communicate your transformational purpose.
  <em>Where are you going? What will you become? Why change now?</em>
</div>
<div class="service" style="left:244px">
  <div class="service-icon"><svg width="46" height="46" viewBox="0 0 46 46" fill="#6ba2c6"><rect x="2" y="2" width="3" height="42"/><rect x="2" y="41" width="42" height="3"/><rect x="9" y="16" width="6" height="22"/><rect x="18" y="8" width="6" height="30"/><rect x="27" y="20" width="6" height="18"/><rect x="36" y="12" width="6" height="26"/></svg></div>
  Assessing the current state of your organization.
  <em>Where are you today? What should be protected and preserved? What needs to change?</em>
</div>
<div class="service" style="left:408px">
  <div class="service-icon"><svg width="44" height="48" viewBox="0 0 44 48" fill="#6ba2c6"><circle cx="22" cy="22" r="10"/><path d="M15 28h14l-3 8h-8z"/><rect x="17" y="37" width="10" height="3"/><rect x="18" y="41" width="8" height="3"/><rect x="21" y="2" width="2" height="6"/><rect x="4" y="19" width="6" height="2"/><rect x="34" y="19" width="6" height="2"/><path d="M9 8l4 4-1 1-4-4zM35 8l-4 4 1 1 4-4z"/></svg></div>
  Building innovative engagements to help people master the skillsets and mindsets needed for your current and future context.
  <em>What programs and projects should be created to ensure your leaders are ready, willing, able and excited to lead the transformation?</em>
</div>
<div class="service" style="left:572px">
  <div class="service-icon"><svg width="48" height="42" viewBox="0 0 48 42"><rect x="3" y="8" width="32" height="32" fill="none" stroke="#6ba2c6" stroke-width="4"/><path d="M10 22l8 8 26-26" fill="none" stroke="#6ba2c6" stroke-width="7"/></svg></div>
  Embedding routines and practices to ensure the transformation is structurally resilient.
  <em>How should future work be divided, done and measured?</em>
</div>
<a class="btn btn-grey approach-btn" href="#">LEARN OUR APPROACH »</a>

<div class="section-head" style="top:828px"><h2>WHO WE ARE</h2></div>
<h2 class="who-title"><b>KESTREL</b> (People-First Strategic Renewal) <strong>ADVISORY</strong></h2>
<div class="who-copy">
  <h3>EXPERIENCED</h3>
  <p>Over the past three decades, we have deep experience driving organizational transformation in more than 33 countries, for some of the world's largest, most transformative companies in your industry.</p>
  <h3>CURIOUS</h3>
  <p>Each of the dozens of transformations we've enabled are unique. Our most relevant experience is our ability to listen and learn where you want to go, and to partner with you to create an original set of tools and experiences to help your people get there. If you're curious, learn more about our team.</p>
  <h3>READY TO HEAR YOUR STORY</h3>
  <p>Of course the best way to get to know more about us is to contact us, get to know us, and see what you think.</p>
</div>
<a class="btn btn-grey team-btn" href="#">MEET THE TEAM »</a>
<a class="btn btn-blue contact-btn" href="#">CONTACT US »</a>

<footer class="site-footer">
  <nav class="footer-nav"><a href="#">ABOUT KESTREL</a><a href="#">APPROACH</a><a href="#">TEAM</a><a href="#">CONTACT</a></nav>
  <div class="social"><span></span><span></span><span></span></div>
  <p class="contact-line">P: 1-800-555-0142 &nbsp;|&nbsp; info@kestreladvisory.com &nbsp;|&nbsp; 215 Harbor Street New York, NY 10013</p>
  <p class="copyright">©2015 KESTREL ADVISORY.</p>
</footer>
</body>
</html>
```